Managed IT Services Marketing Mailer / Handout Project

We are a 21 year old Managed Services Provider (we are the IT department for our clients), and we are looking to increase our client portfolio.

The cards we are looking to design are meant to be used either as a mailer or a handout. This is a trail project that could well turn into a steady, ongoing demand for additional items.

We uploaded our logo in both jpeg as well as jpeg. If you require an alternate format please advise.

Our tag line is: Fast. Secure. Reliable.

Also provided a shot of our office, which we will be replacing with a better quality shot including one of our service vans.

Also included is a PDF proof of a rack card that we developed in order to write and gauge the amount of content. The proof design is not what we are looking - it is stodgy, and we are looking for something modern and crisp. The typeface is also just for text development - something easier to read is preferred.

SIZE: Standard 5x7 inches

Target Market(s)

Small and medium business owners (5 - 75 employees) who do not have in house IT support.

Logo Text

Logo provided

Logo styles of interest
Abstract Logo
Font styles to use
Sans Serif

Colors

Designer to choose colors to be used in the design.

Requirements
Must have
• Tag line, a call to action, one (?) photo, location, contact number, descriptive text and logo.
Nice to have
• No ideas...
Should not have
• Should not be crowded, simpler is better if the offering and the call to action are presented well. It's a pretty simple concept and should be able to be understood by small business owners in 1 minute or less.

```html
<!DOCTYPE html>
<html lang="en">
<head>
<meta charset="utf-8">
<title>Northgate IT – Mailer Card</title>
<link rel="stylesheet" href="https://fonts.googleapis.com/css2?family=Montserrat:wght@400;700;800&family=Didact+Gothic&display=swap">
<style>
  :root {
    --navy: #0d2a5e;
    --navy-deep: #081d45;
    --orange: #f07b14;
    --grey: #7a7f88;
    --paper: #ffffff;
    --backdrop: #eceef1;
    --photo-light: #b9d3ee;
    --photo-mid: #4f86c6;
    --photo-dark: #16407f;
    --rule: #9aa0a8;
  }
  * { box-sizing: border-box; margin: 0; padding: 0; }
  html, body { width: 689px; height: 1200px; overflow: hidden; }
  body {
    background: var(--backdrop);
    font-family: "Didact Gothic", "Century Gothic", sans-serif;
    color: var(--navy);
    position: relative;
  }
  .card {
    position: absolute;
    left: 45px;
    width: 600px;
    height: 428px;
    background: var(--paper);
    box-shadow: 0 6px 18px rgba(0,0,0,.18);
    overflow: hidden;
  }
  .card--front { top: 90px; }
  .card--back { top: 600px; }

  /* Front */
  .front-header {
    position: absolute; left: 0; right: 0; top: 0;
    height: 84px;
    background: var(--navy);
    display: flex; align-items: center; justify-content: center;
  }
  .brand {
    display: flex; align-items: center; gap: 8px;
    font-family: "Montserrat", sans-serif;
    font-weight: 700;
    font-size: 24px;
    line-height: 1;
    color: var(--paper);
  }
  .brand__mark { width: 14px; height: 14px; background: var(--orange); }
  .brand--dark { color: var(--navy); font-size: 19px; }
  .front-photo {
    position: absolute; left: 0; right: 0; top: 90px;
    height: 232px;
    background: linear-gradient(120deg, var(--photo-dark) 0%, var(--photo-mid) 35%, var(--photo-light) 60%, var(--photo-mid) 85%, var(--photo-dark) 100%);
  }
  .front-copy { position: absolute; left: 0; right: 0; top: 330px; text-align: center; }
  .tagline {
    font-family: "Montserrat", sans-serif;
    font-size: 32px; line-height: 34px; letter-spacing: .5px;
  }
  .tagline__strong { color: var(--orange); font-weight: 800; }
  .tagline__light { color: var(--grey); font-weight: 400; }
  .lead {
    font-family: "Montserrat", sans-serif;
    font-weight: 700; font-size: 11.5px; line-height: 14px;
    margin-top: 2px; color: var(--navy-deep);
  }
  .sublead { font-size: 11.5px; line-height: 14px; color: var(--navy-deep); }
  .sublead strong { color: var(--orange); font-family: "Montserrat", sans-serif; font-weight: 700; }
  .contact-line { margin-top: 6px; font-size: 11.5px; line-height: 14px; color: var(--navy); }
  .contact-line .sep { margin: 0 4px; }
  .footer-stripe {
    position: absolute; left: 0; right: 0; bottom: 0; height: 6px;
    background: linear-gradient(90deg, var(--navy) 0 68%, var(--orange) 68% 100%);
  }

  /* Back */
  .back-panel {
    position: absolute; left: 0; top: 0; bottom: 0; width: 325px;
    color: var(--paper);
  }
  .back-photo {
    position: absolute; inset: 0;
    background: linear-gradient(180deg, var(--navy) 0%, #2d3d6a 35%, #7a4a2a 70%, #c46a1f 100%);
  }
  .back-text {
    position: absolute; inset: 0;
    padding: 18px 16px 0 14px;
    font-size: 10.2px; line-height: 1.3;
  }
  .back-text strong { font-family: "Montserrat", sans-serif; font-weight: 700; }
  .back-text .accent { color: var(--orange); font-family: "Montserrat", sans-serif; font-weight: 700; }
  .section-title {
    margin-top: 14px;
    font-family: "Montserrat", sans-serif;
    font-size: 17px; font-weight: 400;
    display: inline-block;
    border-bottom: 2px solid var(--orange);
    padding-bottom: 1px;
  }
  .section-title .accent { font-weight: 800; }
  .points { list-style: none; margin-top: 12px; }
  .points li { position: relative; padding-left: 20px; margin-bottom: 10px; }
  .points li::before {
    content: ""; position: absolute; left: 2px; top: 2px;
    width: 7px; height: 7px; background: var(--orange);
  }
  .back-contact {
    position: absolute; left: 14px; right: 12px; bottom: 12px;
    display: flex; align-items: flex-end; justify-content: space-between;
    font-size: 10.5px; line-height: 1.25;
    color: var(--paper);
  }
  .address { display: flex; gap: 5px; }
  .address strong { display: block; font-family: "Montserrat", sans-serif; font-weight: 700; }
  .phone {
    display: flex; align-items: center; gap: 4px;
    font-family: "Montserrat", sans-serif; font-weight: 700; font-size: 12px;
    border-left: 1px solid rgba(255,255,255,.6); padding-left: 8px;
  }
  .mail-side { position: absolute; left: 325px; right: 0; top: 0; bottom: 0; }
  .mail-side .brand { position: absolute; left: 14px; top: 28px; }
  .stamp-box {
    position: absolute; right: 16px; top: 16px;
    width: 84px; height: 82px; border: 1px solid var(--navy-deep);
  }
  .address-lines { position: absolute; left: 34px; right: 16px; top: 256px; }
  .address-lines div { height: 40px; border-bottom: 1px solid var(--rule); }
</style>
</head>
<body>

<section class="card card--front" aria-label="Mailer front">
  <header class="front-header">
    <div class="brand"><span>Northgate IT</span><span class="brand__mark"></span></div>
  </header>
  <div class="front-photo" role="img" aria-label="Photo of hands typing on a laptop with a glowing network overlay"></div>
  <div class="front-copy">
    <h1 class="tagline"><span class="tagline__strong">FAST SECURE</span> <span class="tagline__light">RELIABLE</span></h1>
    <p class="lead">PROVIDING PROFESSIONAL</p>
    <p class="sublead">IT NETWORK SERVICE TO BUSINESS FOR <strong>OVER 21 YEARS</strong></p>
    <p class="contact-line"><span>www.northgateit.com</span><span class="sep">|</span><span>info@northgateit.com</span></p>
  </div>
  <div class="footer-stripe"></div>
</section>

<section class="card card--back" aria-label="Mailer back">
  <div class="back-panel">
    <div class="back-photo" role="img" aria-label="Photo of the company office building at dusk"></div>
    <div class="back-text">
      <p>Experience our industry <strong>leading and friendly</strong> customer service. No other solutions provider can match our super quick response time, extraordinary customer support, or our ability to deliver <span class="accent">common sense</span> technology solutions that work exactly how you expect them to.</p>
      <h2 class="section-title"><span class="accent">ABOUT</span> US</h2>
      <ul class="points">
        <li>For over 21 years our team of professionals, all possessing numerous certifications and highly recognizable accreditations, routinely provides sound technology solutions and support to businesses of all sizes.</li>
        <li>Our goal is to make your daily operations more focused and effective. We streamline your systems and processes to make them more efficient, eliminate unnecessary security risks and deploy proven methods to help employees become more productive.</li>
        <li>You won't find a "one size fits all" approach here. With industry-specific solutions, our clients continue to gain a competitive advantage. With Northgate IT, access to critical data is faster and more secure than ever before.</li>
      </ul>
    </div>
    <div class="back-contact">
      <div class="address">
        <svg width="11" height="14" viewBox="0 0 12 16" aria-hidden="true"><path d="M6 0a6 6 0 0 0-6 6c0 4.5 6 10 6 10s6-5.5 6-10a6 6 0 0 0-6-6z" fill="#fff"/><circle cx="6" cy="6" r="2.3" fill="#7a4a2a"/></svg>
        <div><strong>Northgate IT</strong>4210 Harbor Crest Road,<br>Suite B, Bayview, CA 92150</div>
      </div>
      <div class="phone">
        <svg width="11" height="11" viewBox="0 0 16 16" aria-hidden="true"><path d="M3.5 1 6 4 4.6 5.6a9 9 0 0 0 5.8 5.8L12 10l3 2.5-1.4 2.4C7 15 1 9 1.1 2.4z" fill="#fff"/></svg>
        <span>(555) 014-2290</span>
      </div>
    </div>
  </div>
  <div class="mail-side">
    <div class="brand brand--dark"><span>Northgate IT</span><span class="brand__mark"></span></div>
    <div class="stamp-box" aria-label="Stamp area"></div>
    <div class="address-lines"><div></div><div></div><div></div></div>
  </div>
</section>

</body>
</html>
```